New Website for NY and South Florida Based Accounting Firm

Accounting and Audit firm located in New York and South Florida needs a website redesign after acquiring new businesses and adding new services.

Our current website can be found here:
http://www.trqbnllp.example/

We have merged with this firm:
http://hollisbarkerwendtfield.example/

We are looking for a comprehensive design that will highlight the firm's dual locations. The final design should communicate security, strength, and growth. We would like to keep our pyramid logo as seen on the trqbnllp.example website, as this has been our logo for over 20 years.

Industry/Entity Type

Accounting

Number of Pages Required

1 page

Font styles to use
Serif
Sans Serif

```html
<!DOCTYPE html>
<html lang="en">
<head>
<meta charset="utf-8">
<title>Tremont, Quill, Bassano &amp; Niles, LLP</title>
<link rel="stylesheet" href="https://fonts.googleapis.com/css2?family=Rokkitt:wght@400;500;600&family=Alegreya+Sans+SC:wght@400&display=swap">
<style>
  :root {
    --navy: #0e2263;
    --ink: #1b1b1b;
    --muted: #6a6a6a;
    --nav-bg: #f4f4f4;
    --footer-bg: #efefef;
    --line: #e2e2e2;
    --white: #ffffff;
  }
  * { margin: 0; padding: 0; box-sizing: border-box; }
  html, body { width: 945px; height: 1200px; overflow: hidden; background: var(--white); }
  body { position: relative; font-family: "Rokkitt", Georgia, serif; color: var(--ink); }

  .site-header { position: absolute; left: 0; top: 0; width: 945px; height: 62px; background: var(--nav-bg); }
  .brand { position: absolute; left: 28px; top: 14px; width: 184px; text-align: center;
    font-family: "Alegreya Sans SC", Arial, sans-serif; font-size: 14px; line-height: 17px; color: var(--navy); }
  .main-nav a { position: absolute; top: 0; height: 62px; line-height: 66px; font-size: 11px; font-weight: 500;
    letter-spacing: .3px; color: var(--navy); text-decoration: none; white-space: nowrap; }
  .main-nav a.is-active { background: var(--navy); color: var(--white); width: 56px; text-align: center; }

  .hero { position: absolute; left: 0; top: 62px; width: 945px; height: 436px;
    background: linear-gradient(180deg, #4b4f56 0%, #3a3d42 35%, #2a2c31 70%, #1f2126 100%); }
  .hero-tagline { position: absolute; left: 140px; top: 178px; width: 665px; text-align: center;
    font-size: 24.5px; line-height: 36px; color: var(--white); letter-spacing: .2px; }
  .hero-arrow { position: absolute; top: 248px; }
  .hero-shadow { position: absolute; left: 0; top: 498px; }

  .section-title { position: absolute; left: 0; top: 534px; width: 945px; text-align: center;
    font-size: 36px; font-weight: 400; }
  .section-title span { color: var(--navy); }

  .service-card { position: absolute; top: 643px; width: 283px; height: 216px;
    border: 1px solid var(--line); background: var(--white); text-align: center; }
  .service-card.is-featured { border-color: var(--navy); }
  .service-icon { display: block; margin: 23px auto 0; }
  .service-card h3 { margin-top: 15px; font-size: 18px; font-weight: 500; line-height: 22px; }
  .service-card p { margin: 5px auto 0; width: 250px; font-size: 10.5px; line-height: 13px; color: var(--muted); }
  .read-more { display: inline-block; margin-top: 9px; font-size: 10.5px; color: #333; letter-spacing: .2px; }
  .is-featured .read-more { color: var(--navy); }
  .read-more::after { content: ""; display: inline-block; margin-left: 5px; border-left: 4px solid currentColor;
    border-top: 3.5px solid transparent; border-bottom: 3.5px solid transparent; }

  .site-footer { position: absolute; left: 0; top: 916px; width: 945px; height: 215px; background: var(--footer-bg); }
  .footer-col { position: absolute; top: 0; }
  .footer-col h4 { margin-top: 33px; font-size: 13.5px; font-weight: 400; color: var(--navy); letter-spacing: .2px; }
  .footer-about { left: 46px; width: 285px; }
  .footer-about p { margin-top: 15px; font-size: 10px; line-height: 15px; text-align: justify; color: #333; }
  .btn { display: block; background: var(--navy); color: var(--white); font-size: 10.5px; text-align: center; font-weight: 500; }
  .footer-about .btn { margin-top: 11px; width: 99px; height: 30px; line-height: 30px; }
  .footer-divider { position: absolute; top: 52px; width: 1px; height: 120px; background: #e0e0e0; }
  .footer-news { left: 404px; width: 266px; }
  .footer-news h4 { margin-top: 35px; }
  .footer-news p { margin-top: 14px; font-size: 9.5px; line-height: 13.5px; text-align: justify; color: #222; }
  .email-field { margin: 19px 0 0 2px; width: 264px; height: 28px; background: var(--white);
    font-size: 8px; color: #b0b0b0; line-height: 28px; padding-left: 10px; }
  .footer-news .btn { margin: 12px 0 0 2px; width: 264px; height: 28px; line-height: 29px; }
  .footer-location { left: 737px; width: 180px; }
  .social-link { position: absolute; left: 3px; display: flex; align-items: center; gap: 14px;
    font-size: 13.5px; letter-spacing: .3px; color: #555; white-space: nowrap; }
  .social-link .dot { width: 30px; height: 30px; border-radius: 50%; border: 1px solid #9a9a9a; }
  .social-link.is-primary { color: var(--navy); }
  .social-link.is-primary .dot { background: var(--navy); border-color: var(--navy); }

  .legal-bar { position: absolute; left: 0; top: 1131px; width: 945px; height: 69px; background: var(--navy);
    color: var(--white); text-align: center; font-size: 8.5px; font-weight: 600; line-height: 70px; letter-spacing: .2px; }
</style>
</head>
<body>
  <header class="site-header">
    <div class="brand">Tremont, Quill, Bassano<br>&amp; Niles, LLP</div>
    <nav class="main-nav">
      <a class="is-active" style="left:233px">HOME</a>
      <a style="left:322px">WHY TQBN?</a>
      <a style="left:433px">SERVICE</a>
      <a style="left:522px">PROFILES</a>
      <a style="left:618px">TIPS &amp; LINKS</a>
      <a style="left:732px">CLIENT LOGIN</a>
      <a style="left:854px">CONTACT</a>
    </nav>
  </header>

  <section class="hero" role="img" aria-label="Dusk photograph of a dense city skyline seen from above">
    <svg class="hero-arrow" style="left:20px" width="20" height="50" viewBox="0 0 20 50"><polyline points="17,1 3,25 17,49" fill="none" stroke="#fff" stroke-width="1.5"/></svg>
    <p class="hero-tagline">WE USE OUR VAST ARRAY OF RESOURCES, DEPTH OF KNOWLEDGE AND EXPERIENCE TO POSITION YOU FOR SUCCESS, STABILITY AND PROSPERITY.</p>
    <svg class="hero-arrow" style="left:904px" width="20" height="50" viewBox="0 0 20 50"><polyline points="3,1 17,25 3,49" fill="none" stroke="#fff" stroke-width="1.5"/></svg>
  </section>
  <svg class="hero-shadow" width="945" height="36" viewBox="0 0 945 36">
    <defs><radialGradient id="shade" cx="50%" cy="0%" r="50%" fx="50%" fy="0%"><stop offset="0" stop-color="#000" stop-opacity=".22"/><stop offset="1" stop-color="#000" stop-opacity="0"/></radialGradient></defs>
    <ellipse cx="472" cy="0" rx="470" ry="34" fill="url(#shade)"/>
  </svg>

  <h2 class="section-title">Our <span>Service</span></h2>

  <article class="service-card" style="left:37px">
    <svg class="service-icon" width="62" height="62" viewBox="0 0 62 62"><circle cx="31" cy="31" r="30" fill="none" stroke="#0e2263" stroke-width="1.2"/><text x="31" y="42" text-anchor="middle" font-family="Arial, sans-serif" font-weight="700" font-size="32" fill="#0e2263">$</text></svg>
    <h3>Accounting &amp; Auditing</h3>
    <p>Lorem ipsum dolor sit amet, consectetur adipiscing elit, sed do eiusmod tempor incididunt ut labore et dolore magna aliqua.</p>
    <span class="read-more">READ MORE</span>
  </article>
  <article class="service-card is-featured" style="left:330px">
    <svg class="service-icon" width="62" height="62" viewBox="0 0 62 62"><circle cx="31" cy="31" r="31" fill="#0e2263"/><path d="M21 17h14l7 7v22H21z" fill="none" stroke="#fff" stroke-width="2"/><path d="M35 17v7h7" fill="none" stroke="#fff" stroke-width="2"/><path d="M26 30h11M26 35h11M26 40h11" stroke="#fff" stroke-width="2"/></svg>
    <h3>Financial Planning</h3>
    <p>Lorem ipsum dolor sit amet, consectetur adipiscing elit, sed do eiusmod tempor incididunt ut labore et dolore magna aliqua.</p>
    <span class="read-more">READ MORE</span>
  </article>
  <article class="service-card" style="left:623px">
    <svg class="service-icon" width="62" height="62" viewBox="0 0 62 62"><circle cx="31" cy="31" r="30" fill="none" stroke="#0e2263" stroke-width="1.2"/><path d="M15 21h10l3 3h12v5H22l-7 14z" fill="#0e2263"/><path d="M22 31h27l-7 14H15z" fill="#0e2263"/></svg>
    <h3>Tax Services</h3>
    <p>Lorem ipsum dolor sit amet, consectetur adipiscing elit, sed do eiusmod tempor incididunt ut labore et dolore magna aliqua.</p>
    <span class="read-more">READ MORE</span>
  </article>

  <footer class="site-footer">
    <div class="footer-col footer-about">
      <h4>ABOUT US</h4>
      <p>Lorem ipsum dolor sit amet, consectetur adipiscing elit, sed do eiusmod tempor incididunt ut labore et dolore magna aliqua. Ut enim ad minim veniam, quis nostrud exercitation ullamco laboris nisi ut aliquip ex ea commodo consequat.Ut enim ad minim veniam, quis nostrud exercitation ullamco laboris nisi ut aliquip ex ea commodo consequat.</p>
      <span class="btn">READ MORE</span>
    </div>
    <span class="footer-divider" style="left:363px"></span>
    <div class="footer-col footer-news">
      <h4>NEWSLETTER SIGNUP</h4>
      <p>Subscribe our newsletter to know our daily updates and offer daily updates and offer Ut enim ad minim veniam, quis nostrud exercitation</p>
      <div class="email-field">Enter your Email Id</div>
      <span class="btn">SUBSCRIBE</span>
    </div>
    <span class="footer-divider" style="left:703px"></span>
    <div class="footer-col footer-location">
      <h4>LOCATION</h4>
      <span class="social-link is-primary" style="top:70px"><span class="dot"></span>Friendsphere</span>
      <span class="social-link" style="top:116px"><span class="dot"></span>CirclePlus</span>
      <span class="social-link" style="top:159px"><span class="dot"></span>ViewStream</span>
    </div>
  </footer>

  <div class="legal-bar">@ 2016 TQBN LLP. All right Receserved Team of Use</div>
</body>
</html>
```